Willowmere Counseling (Endure - Mend - Flourish) - Double Sided Business Card

I would like a 2-sided business card. Front: Matte Black or Navy with Logo & Tagline. Back: Name, Address, Phone Number, Email, & Website (maybe would like to include a small map pin-pointing location); Prefer front to be a gold/silver foil (iridescent); Back prefer white or light colored background with lettering that is easy to read and simple

Target Market(s)

Individuals & Couples (13 y.o. - ALL Adults); High end clientele

Industry/Entity Type

Licensed Professional Counselor (Mental Health)

Contact Information for Business Card

Name: Willowmere Counseling; Tagline: Endure - Mend - Flourish; Address: 3870 N. Garrick Ave., Suite 214, Fort Worth, TX 76132; Phone: (214) 555-0187; Website: www.WillowmereCounseling.example

Font styles to use
Serif

Requirements
Must have
• Logo on Front (Large) prefer gold/silver foil on a matte dark color (i.e. black, navy, etc.); Back of Card: All other relevant information

```html
<!DOCTYPE html>
<html lang="en">
<head>
<meta charset="utf-8">
<title>Willowmere Counseling – Business Card</title>
<link href="https://fonts.googleapis.com/css2?family=Cinzel:wght@400;600&family=Tinos&display=swap" rel="stylesheet">
<style>
  :root {
    --backdrop: #2a2a2b;
    --card-grey: #808184;
    --gold: #d4b452;
    --gold-deep: #c9a43c;
    --white: #ffffff;
    --ink-grey: #6d6e71;
    --shadow: rgba(0,0,0,0.45);
  }
  * { margin: 0; padding: 0; box-sizing: border-box; }
  html, body { width: 1200px; height: 900px; overflow: hidden; background: var(--backdrop); }
  .stage { position: relative; width: 1200px; height: 900px; }

  .card {
    position: absolute;
    width: 620px; height: 354px;
    border-radius: 24px;
    overflow: hidden;
    box-shadow: 0 10px 28px var(--shadow);
  }

  /* Front side */
  .card-front { left: 70px; top: 70px; background: var(--card-grey); }
  .front-brand {
    position: absolute; inset: 0;
    display: flex; align-items: center; justify-content: center; gap: 18px;
  }
  .brand-dot {
    width: 54px; height: 54px; border-radius: 50%;
    background: var(--gold);
    flex: none;
  }
  .brand-text { display: flex; flex-direction: column; align-items: center; }
  .brand-name {
    font-family: "Cinzel", serif; font-weight: 600;
    color: var(--gold); font-size: 38px; line-height: 1.05; letter-spacing: 1px;
    text-align: center;
  }
  .brand-rule { width: 100%; height: 2px; background: var(--gold); margin: 8px 0 6px; }
  .brand-tagline {
    font-family: "Cinzel", serif; font-weight: 400;
    color: var(--gold); font-size: 14px; letter-spacing: 1.5px;
  }

  /* Back side */
  .card-back { left: 510px; top: 476px; background: var(--white); }
  .back-waves { position: absolute; inset: 0; }
  .back-brand {
    position: absolute; left: 34px; top: 92px;
    display: flex; align-items: center; gap: 14px;
    z-index: 1;
  }
  .back-brand .brand-dot { width: 42px; height: 42px; }
  .back-brand .brand-name { font-size: 27px; }
  .back-brand .brand-rule { background: var(--ink-grey); margin: 6px 0 5px; }
  .back-brand .brand-tagline { font-size: 11px; letter-spacing: 1px; }

  .holder { position: absolute; right: 36px; top: 34px; text-align: right; z-index: 1; }
  .holder-name {
    font-family: "Cinzel", serif; font-size: 19px; letter-spacing: 1.5px; color: var(--ink-grey);
  }
  .holder-role {
    font-family: "Cinzel", serif; font-size: 12.5px; letter-spacing: 1.5px; color: var(--gold-deep);
    margin-top: 2px;
  }

  .contact { position: absolute; right: 22px; bottom: 26px; list-style: none; z-index: 1; }
  .contact li {
    display: flex; justify-content: flex-end; align-items: center; gap: 9px;
    font-family: "Tinos", serif; font-size: 14px; color: var(--white);
    line-height: 23px;
  }
  .contact svg { width: 14px; height: 14px; flex: none; }
</style>
</head>
<body>
<main class="stage">

  <section class="card card-front" aria-label="Card front">
    <div class="front-brand">
      <span class="brand-dot"></span>
      <div class="brand-text">
        <div class="brand-name">WILLOWMERE<br>COUNSELING</div>
        <div class="brand-rule"></div>
        <div class="brand-tagline">ENDURE - MEND - FLOURISH</div>
      </div>
    </div>
  </section>

  <section class="card card-back" aria-label="Card back">
    <svg class="back-waves" viewBox="0 0 620 354" preserveAspectRatio="none" aria-hidden="true">
      <path d="M0,250 C180,250 300,200 390,160 C460,128 540,114 620,108 L620,124 C540,130 470,146 410,178 C320,226 190,268 0,268 Z" fill="var(--gold)"/>
      <path d="M0,284 C200,284 330,240 420,196 C480,166 550,146 620,140 L620,354 L0,354 Z" fill="var(--card-grey)"/>
      <path d="M0,322 C230,312 360,262 440,220 C500,188 560,168 620,160" fill="none" stroke="var(--white)" stroke-width="2"/>
    </svg>

    <div class="back-brand">
      <span class="brand-dot"></span>
      <div class="brand-text">
        <div class="brand-name">WILLOWMERE<br>COUNSELING</div>
        <div class="brand-rule"></div>
        <div class="brand-tagline">ENDURE - MEND - FLOURISH</div>
      </div>
    </div>

    <div class="holder">
      <div class="holder-name">MARISOL PENNOCK, MS</div>
      <div class="holder-role">LPC - OWNER/CLINICIAN</div>
    </div>

    <ul class="contact">
      <li>(214) 555-0187
        <svg viewBox="0 0 24 24"><path d="M6.6 10.8a15 15 0 0 0 6.6 6.6l2.2-2.2c.3-.3.7-.4 1-.2 1.1.4 2.3.6 3.6.6.6 0 1 .4 1 1V20c0 .6-.4 1-1 1A17 17 0 0 1 3 4c0-.6.4-1 1-1h3.5c.6 0 1 .4 1 1 0 1.3.2 2.5.6 3.6.1.3 0 .7-.2 1z" fill="var(--gold)"/></svg>
      </li>
      <li>info@WillowmereCounseling.example
        <svg viewBox="0 0 24 24"><rect x="2" y="5" width="20" height="14" rx="1" fill="var(--gold)"/><path d="M2 6l10 7 10-7" fill="none" stroke="var(--card-grey)" stroke-width="1.6"/></svg>
      </li>
      <li>www.WillowmereCounseling.example
        <svg viewBox="0 0 24 24" fill="none" stroke="var(--gold)" stroke-width="1.8"><circle cx="12" cy="12" r="9.5"/><ellipse cx="12" cy="12" rx="4" ry="9.5"/><path d="M2.5 12h19M4 7h16M4 17h16"/></svg>
      </li>
      <li>3870 N. Garrick Ave., Suite 214, Fort Worth, TX 76132
        <svg viewBox="0 0 24 24"><path d="M12 2a7 7 0 0 0-7 7c0 5 7 13 7 13s7-8 7-13a7 7 0 0 0-7-7z" fill="var(--gold)"/><circle cx="12" cy="9" r="2.6" fill="var(--card-grey)"/></svg>
      </li>
    </ul>
  </section>

</main>
</body>
</html>
```